Business Card Design - Carrington Hill Lodge

We are looking at a new design for our business cards that has a modern and professional look. We run a residential aged care facility focussing on the care of residents. The cards will be used for potential clients, consultants and business opportunities in this sector. Blue and white is our main colours and would to see these colours incorporated in the design.
Industry/Entity Type
Business
Contact Information for Business Card
Carrington Hill Lodge, Darren Pelham, dpelham@carringtonhilllodge.com.au, Finance Manager, 0491 736 208, BCom, 48 Yarrabee Way, Ashgrove Vale, QLD 4521.

```html
<!DOCTYPE html>
<html lang="en">
<head>
<meta charset="utf-8">
<title>Carrington Hill Lodge – Business Card</title>
<link rel="stylesheet" href="https://fonts.googleapis.com/css2?family=Open+Sans:ital,wght@0,400;0,700;1,400&family=Oswald:wght@300&display=swap">
<style>
  :root {
    --card-bg: #dce8eb;
    --brand-blue: #527a8f;
    --band-taupe: #a69d91;
    --ink: #141414;
    --ink-soft: #1f2a30;
    --white: #ffffff;
  }
  * { margin: 0; padding: 0; box-sizing: border-box; }
  html, body {
    width: 726px;
    height: 1200px;
    overflow: hidden;
    background: var(--card-bg);
  }
  .card {
    position: relative;
    width: 726px;
    height: 1200px;
    background: var(--card-bg);
    font-family: "Open Sans", Arial, sans-serif;
    color: var(--ink);
  }
  .brand-mark {
    position: absolute;
    left: 50%;
    top: 110px;
    width: 300px;
    height: 300px;
    margin-left: -150px;
    border-radius: 50%;
    background: var(--brand-blue);
  }
  .brand-name {
    position: absolute;
    left: 0;
    right: 0;
    top: 428px;
    text-align: center;
    font-family: "Oswald", "Arial Narrow", sans-serif;
    font-weight: 300;
    font-size: 64px;
    line-height: 1;
    letter-spacing: 2px;
    color: var(--ink-soft);
    white-space: nowrap;
  }
  .tagline-band {
    position: absolute;
    left: 0;
    top: 512px;
    width: 100%;
    height: 59px;
    background: var(--band-taupe);
    display: flex;
    align-items: center;
    padding-left: 54px;
  }
  .tagline {
    font-style: italic;
    font-size: 40px;
    color: var(--white);
    white-space: nowrap;
  }
  .contact {
    position: absolute;
    left: 82px;
    top: 630px;
  }
  .person-name {
    font-weight: 700;
    font-size: 35px;
    line-height: 44px;
  }
  .qualification {
    font-weight: 400;
    font-style: italic;
    font-size: 25px;
  }
  .job-title {
    font-style: italic;
    font-size: 31px;
    line-height: 46px;
  }
  .phone {
    margin-top: 80px;
    font-size: 31px;
    line-height: 44px;
  }
  .phone strong {
    font-weight: 700;
    font-size: 34px;
  }
  .email {
    font-size: 30px;
    line-height: 54px;
    white-space: nowrap;
  }
  .address-band {
    position: absolute;
    left: 0;
    bottom: 0;
    width: 100%;
    height: 238px;
    background: var(--band-taupe);
    padding-top: 46px;
    text-align: center;
  }
  .address {
    font-style: normal;
    font-weight: 700;
    font-size: 37px;
    line-height: 48px;
    color: var(--ink);
  }
</style>
</head>
<body>
  <div class="card">
    <div class="brand-mark" aria-hidden="true"></div>
    <h1 class="brand-name">CARRINGTON HILL LODGE</h1>

    <div class="tagline-band">
      <p class="tagline">Comfort, Respect, Companionship</p>
    </div>

    <div class="contact">
      <p class="person-name">Darren Pelham <span class="qualification">BCom.</span></p>
      <p class="job-title">Finance Manager</p>
      <p class="phone">mobile: <strong>0491 736 208</strong></p>
      <p class="email">dpelham@carringtonhilllodge.com.au</p>
    </div>

    <div class="address-band">
      <address class="address">48 YARRABEE WAY,<br>ASHGROVE VALE, QLD 4521.</address>
    </div>
  </div>
</body>
</html>
```